Symposium Flyer

I need a flyer for advertising an upcoming symposium titled, "Stirring and settling the chromatin map", I am organizing as well as a webpage design for the symposium. The Symposium is taking place on Thursday, February 7th, 2019 at the Halvorsen College Dunmere School of Medicine. It is being held by the Genomic Regulation Collegium at the Vantreck Hall for Applied Discovery (Kellaway Auditorium and Lobby, 2750 Orchard Terrace Way, Philadelphia, PA 19187). You can view previous symposiums from our institution at https://events.hdsm-example.org/genreg/meetings/

Our Keynote speakers for this symposium are:
Ottokar Brummell, M.D., Professor of Biology at the Northvale Polytechnic of Applied Science; Founding Member of the Corriveau Foundation for Life Science Study; Member of the Council of Clinical Scholars.
AND
Thomas (Tom) Weylund, M.D., President of the Lumavex Centers for Therapeutic Discovery (LCTD)

We will be adding 8 more speakers to this event, so please leave room for extra speakers to be added and for a website registration link and QR code to be added.

Please email me should have additional questions - corvi@hdsm-example.org

```html
<!DOCTYPE html>
<html lang="en">
<head>
<meta charset="utf-8">
<title>Stirring and Settling the Chromatin Map — Symposium Flyer</title>
<link href="https://fonts.googleapis.com/css2?family=Hind:wght@500;600;700&family=PT+Serif:ital,wght@0,700;1,400&display=swap" rel="stylesheet">
<style>
  :root {
    --page-bg: #e9e6e2;
    --paper: #ffffff;
    --ink-black: #050608;
    --red-top: #d3232a;
    --red-bottom: #6e0707;
    --blue-top: #0d4a97;
    --blue-bottom: #1c6ab8;
    --name-blue: #1d4f94;
    --text-grey: #3a3a3a;
    --footer-grey: #e4e5e7;
    --arrow-red: #c4151c;
  }
  * { margin: 0; padding: 0; box-sizing: border-box; }
  html, body { width: 1002px; height: 1200px; overflow: hidden; background: var(--page-bg); }
  .flyer {
    position: absolute; left: 76px; top: 0;
    width: 850px; height: 1200px;
    background: linear-gradient(180deg, #fff 0%, #fff 62%, #f3f3f4 64%, #fff 70%);
    overflow: hidden;
    font-family: "Hind", Arial, sans-serif;
  }
  .hero-shapes { position: absolute; left: 0; top: 0; width: 850px; height: 760px; }
  .hero-visual {
    position: absolute; left: 34px; top: 35px; width: 411px; height: 523px;
    background: radial-gradient(ellipse 55% 38% at 52% 46%, #7a3fb0 0%, #3b2d8e 35%, #0f5b78 58%, #050608 80%);
    clip-path: polygon(0 0, 100% 0, 100% 465px, 0 100%);
  }
  .headline-panel {
    position: absolute; left: 473px; top: 56px; width: 300px; color: #fff;
  }
  .headline {
    font-weight: 700; font-size: 37px; line-height: 1.2; text-transform: uppercase; letter-spacing: 0.2px;
  }
  .date {
    margin-top: 26px; font-weight: 600; font-size: 25px; line-height: 1.25; text-transform: uppercase;
  }
  .date .suffix { text-transform: none; }
  .host { margin-top: 20px; font-weight: 600; font-size: 24px; line-height: 1.25; }
  .venue {
    position: absolute; left: 473px; top: 590px; width: 300px; color: #fff;
    font-weight: 600; font-size: 16.5px; line-height: 1.25;
  }
  .venue p + p { margin-top: 20px; }
  .speaker-list { position: absolute; list-style: none; width: 345px; }
  .speaker-list.left { left: 71px; top: 627px; }
  .speaker-list.right { left: 451px; top: 761px; }
  .speaker { margin-bottom: 12px; }
  .speaker-name {
    font-family: "PT Serif", Georgia, serif; font-weight: 700; font-size: 18.5px; color: var(--name-blue);
    display: flex; align-items: center; gap: 9px; line-height: 1.2; margin-left: -30px;
  }
  .speaker-name svg { flex: none; width: 20px; height: 20px; }
  .speaker-role {
    font-family: "PT Serif", Georgia, serif; font-style: italic; font-size: 10.2px; line-height: 1.38;
    color: var(--text-grey); margin-top: 4px;
  }
  .footer-band { position: absolute; left: 0; top: 1071px; width: 850px; height: 129px; background: var(--footer-grey); }
  .footer-shapes { position: absolute; left: 0; top: 1050px; width: 850px; height: 150px; }
  .partner {
    position: absolute; top: 1104px; display: flex; align-items: center; gap: 10px;
    font-family: "Hind", Arial, sans-serif; font-weight: 600; font-size: 19px; line-height: 1.1; color: var(--name-blue);
  }
  .partner .mark { width: 26px; height: 26px; border-radius: 50%; background: var(--name-blue); flex: none; }
  .partner.collegium { left: 318px; width: 210px; }
  .partner.school { left: 550px; width: 250px; }
</style>
</head>
<body>
<main class="flyer">
  <svg class="hero-shapes" viewBox="0 0 850 760" aria-hidden="true">
    <defs>
      <linearGradient id="redPanel" x1="0" y1="0" x2="0" y2="1">
        <stop offset="0" stop-color="#d3232a"/>
        <stop offset="1" stop-color="#6e0707"/>
      </linearGradient>
      <linearGradient id="bluePanel" x1="0" y1="0" x2="0" y2="1">
        <stop offset="0" stop-color="#0d4a97"/>
        <stop offset="1" stop-color="#1c6ab8"/>
      </linearGradient>
    </defs>
    <polygon points="34,35 815,35 815,476 34,558" fill="#050608"/>
    <polygon points="445,35 783,35 783,512 445,544" fill="url(#redPanel)"/>
    <polygon points="445,547 783,515 783,740 445,740" fill="url(#bluePanel)"/>
    <line x1="445" y1="545.5" x2="783" y2="513.5" stroke="#fff" stroke-width="3"/>
    <circle cx="612" cy="530" r="43" fill="#fff"/>
    <polyline points="594,520 612,538 630,520" fill="none" stroke="#c4151c" stroke-width="8" stroke-linecap="square"/>
  </svg>

  <div class="hero-visual" role="img" aria-label="Rendered molecular model of DNA strands wrapped around histone proteins, glowing cyan and purple on black"></div>

  <section class="headline-panel">
    <h1 class="headline">Stirring &amp; Settling the Chromatin Map</h1>
    <p class="date">Thursday,<br>February 7<span class="suffix">th</span> 2019</p>
    <p class="host">At The Halvorsen College Dunmere School Of Medicine</p>
  </section>

  <section class="venue">
    <p>Genomic Regulation Collegium At The Vantreck Hall For Applied Discovery</p>
    <p>(Kellaway Auditorium And Lobby, 2750 Orchard Terrace Way, Philadelphia, Pa 19187).</p>
  </section>

  <ul class="speaker-list left">
    <li class="speaker">
      <h2 class="speaker-name"><svg viewBox="0 0 20 20"><circle cx="10" cy="10" r="10" fill="#c4151c"/><polyline points="8,5.5 12.5,10 8,14.5" fill="none" stroke="#fff" stroke-width="2.6"/></svg>Ottokar Brummell, M.D.</h2>
      <p class="speaker-role">Professor of Biology at the Northvale Polytechnic of Applied Science;<br>Founding Member of the Corriveau Foundation for Life Science Study;<br>Member of the Council of Clinical Scholars.</p>
    </li>
    <li class="speaker">
      <h2 class="speaker-name"><svg viewBox="0 0 20 20"><circle cx="10" cy="10" r="10" fill="#c4151c"/><polyline points="8,5.5 12.5,10 8,14.5" fill="none" stroke="#fff" stroke-width="2.6"/></svg>Thomas (Tom) Weylund, M.D.,</h2>
      <p class="speaker-role">President of the Lumavex Centers for Therapeutic Discovery (LCTD)</p>
    </li>
    <li class="speaker">
      <h2 class="speaker-name"><svg viewBox="0 0 20 20"><circle cx="10" cy="10" r="10" fill="#c4151c"/><polyline points="8,5.5 12.5,10 8,14.5" fill="none" stroke="#fff" stroke-width="2.6"/></svg>Name here name here</h2>
      <p class="speaker-role">Professor of Biology at the Northvale Polytechnic of Applied Science;<br>Founding Member of the Corriveau Foundation for Life Science Study;<br>Member of the Council of Clinical Scholars.</p>
    </li>
    <li class="speaker">
      <h2 class="speaker-name"><svg viewBox="0 0 20 20"><circle cx="10" cy="10" r="10" fill="#c4151c"/><polyline points="8,5.5 12.5,10 8,14.5" fill="none" stroke="#fff" stroke-width="2.6"/></svg>Name here name here</h2>
      <p class="speaker-role">President of the Lumavex Centers for Therapeutic Discovery (LCTD)</p>
    </li>
    <li class="speaker">
      <h2 class="speaker-name"><svg viewBox="0 0 20 20"><circle cx="10" cy="10" r="10" fill="#c4151c"/><polyline points="8,5.5 12.5,10 8,14.5" fill="none" stroke="#fff" stroke-width="2.6"/></svg>Name here name here</h2>
      <p class="speaker-role">Professor of Biology at the Northvale Polytechnic of Applied Science;<br>Founding Member of the Corriveau Foundation for Life Science Study;<br>Member of the Council of Clinical Scholars.</p>
    </li>
    <li class="speaker">
      <h2 class="speaker-name"><svg viewBox="0 0 20 20"><circle cx="10" cy="10" r="10" fill="#c4151c"/><polyline points="8,5.5 12.5,10 8,14.5" fill="none" stroke="#fff" stroke-width="2.6"/></svg>Name here name here</h2>
      <p class="speaker-role">President of the Lumavex Centers for Therapeutic Discovery (LCTD)</p>
    </li>
  </ul>

  <ul class="speaker-list right">
    <li class="speaker">
      <h2 class="speaker-name"><svg viewBox="0 0 20 20"><circle cx="10" cy="10" r="10" fill="#c4151c"/><polyline points="8,5.5 12.5,10 8,14.5" fill="none" stroke="#fff" stroke-width="2.6"/></svg>Name here name here</h2>
      <p class="speaker-role">Professor of Biology at the Northvale Polytechnic of Applied Science;<br>Founding Member of the Corriveau Foundation for Life Science Study;<br>Member of the Council of Clinical Scholars.</p>
    </li>
    <li class="speaker">
      <h2 class="speaker-name"><svg viewBox="0 0 20 20"><circle cx="10" cy="10" r="10" fill="#c4151c"/><polyline points="8,5.5 12.5,10 8,14.5" fill="none" stroke="#fff" stroke-width="2.6"/></svg>Name here name here</h2>
      <p class="speaker-role">President of the Lumavex Centers for Therapeutic Discovery (LCTD)</p>
    </li>
    <li class="speaker">
      <h2 class="speaker-name"><svg viewBox="0 0 20 20"><circle cx="10" cy="10" r="10" fill="#c4151c"/><polyline points="8,5.5 12.5,10 8,14.5" fill="none" stroke="#fff" stroke-width="2.6"/></svg>Name here name here</h2>
      <p class="speaker-role">Professor of Biology at the Northvale Polytechnic of Applied Science;<br>Founding Member of the Corriveau Foundation for Life Science Study;<br>Member of the Council of Clinical Scholars.</p>
    </li>
    <li class="speaker">
      <h2 class="speaker-name"><svg viewBox="0 0 20 20"><circle cx="10" cy="10" r="10" fill="#c4151c"/><polyline points="8,5.5 12.5,10 8,14.5" fill="none" stroke="#fff" stroke-width="2.6"/></svg>Name here name here</h2>
      <p class="speaker-role">President of the Lumavex Centers for Therapeutic Discovery (LCTD)</p>
    </li>
  </ul>

  <div class="footer-band"></div>
  <svg class="footer-shapes" viewBox="0 0 850 150" aria-hidden="true">
    <defs>
      <linearGradient id="footerBlue" x1="0" y1="0" x2="1" y2="1">
        <stop offset="0" stop-color="#0d4a97"/>
        <stop offset="1" stop-color="#1c6ab8"/>
      </linearGradient>
    </defs>
    <path d="M0,0 H220 Q240,0 245,22 L275,150 H0 Z" fill="url(#footerBlue)"/>
  </svg>

  <div class="partner collegium"><span class="mark"></span>Genomic Regulation Collegium</div>
  <div class="partner school"><span class="mark"></span>Halvorsen College Dunmere School of Medicine</div>
</main>
</body>
</html>
```